VORELLE Body Scrub and Lotion Label Design

Need designs for new product line, VORELLE, for a day spa in Houston, TX. We are a Japanese inspired day spa and have been opened for 26 years. We are currently in the process of creating a product line of body scrubs and lotions. The product line represent scents based on the 5 Japanese elements hi (Fire), kaze (Wind), tsuchi (Earth), mizu (Water), and sora (Heaven). The final design should have a cohesive Japanese influence and each label should represent the corresponding element. I will need a 3 inch label for the cap of the jar with name, ingredients, design and size. A 3 inch label for description and instruction on use of product on bottom of jar, a wrap around label for jar with the name of the product & description and size, and a full wrap around label for lotion bottles. Below are the links for each of the containers and jar cap.

Jar - https://www.jarbinsupply.example/item/J049A
Jar cap - https://www.jarbinsupply.example/item/L252
Bottle - https://www.jarbinsupply.example/item/B320A

Description for each element for design inspiration:
火 hi (Fire) - Evoking thoughts of cozying up with a warm cup of chai on a cool autumn night, our 火 hi (Fire) Cleansing Body Scrub embodies the virtue of purity while delivering a decadent experience. Organic Japanese honey crystals, organic Japanese black tea and organic sunflower seed oil, exfoliate and renew parched, rough skin while powerful essential oils increase circulation and flush toxins from the skin. Japanese honey, which contains antibacterial, antiseptic, and antioxidant properties, heals and nourishes while glycolic acid, one of honey’s natural alpha hydroxy acids, exfoliates and smooths the skin. As a humectant, honey also revitalizes and soothes overworked, dehydrated skin. Together these powerful ingredients support the skin’s own cell renewal process, and assist in creating smooth, hydrated skin. Rejuvenate, soften, and restore the natural glow of youthful skin with 火 hi (Fire) Cleansing Body Scrub.

Use: Grab a small amount. Massage gently onto surface of dry skin. Add a small amount of warm water and massage gently again. Rinse with warm water, dry and apply 火 hi (Fire) Body Lotion.

Ingredients: Sucrose (Organic Sugar), Organic Helianthus Annuus (Sunflower) Seed Oil, Organic Honey Crystals (Dried Honey, Cane Juice and Molasses), Organic Camellia Sinensis (Black Tea), Mel (Honey), Citrus Medica Limonum (Lemon) Peel Oil, Citrus Junos (Yuzu) Peel Oil, Eucalyptus Globules Leaf Oil, Eugenia Caryophyllus (Clove) Flower Oil, Cinnamonum Zeylanicum (Cinnamon) Leaf Oil, Rosmarinus Officinalis (Rosemary) Leaf Oil, Tocopherol (Vitamin E).
___________________________

風 kaze (Wind) - Rouse your senses and renew your dull skin with 風 kaze (Wind) Body Scrub. Pure Asian Sea salt and Israeli Dead Sea salt, along with Japanese fruit powders, gently exfoliate to reveal fresher, more vibrant skin. Sweet almond, lavender, and clary sage oils soothe body and mind as lemon peel and oils of rosemary and cajeput heal and improve skin clarity. 風 kaze (Wind) Cleansing Body Scrub also helps protects skin from environmental damage (including UV rays) with the powerful antioxidant, vitamin E. Prepare to show skin that glows with 風 kaze (Wind) Cleansing Body Scrub.

Use: Grab a small amount. Massage gently onto surface of dry skin. Add a small amount of warm water and massage gently again. Rinse with warm water, dry and apply 風 kaze (Wind) Body Lotion.

Ingredients: Sodium Chloride (Asian Sea and Israeli Dead Sea Salt), Prunus Amygdalus Dulcis (Sweet Almond) Oil, Lavandula Angustifolia (Lavender) Buds, Rosmarinus Officinalis (Rosemary) Leaf Oil, Citrus Medica Limonum (Lemon) Peel Powder, Citrus Junos (Yuzu) Peel Oil, Melaleuca Cajeputi (Cajeput) Oil, Lavandula Angustifolia (Lavender) Oil, Luffa Cylindrica (Luffa) Fruit Powder, Salvia Sclarea (Clary) Oil, Baphicacanthus Cusia (Nees) Bremek Powder, Tocopherol (Vitamin E).
____________________________

地 tsuchi (Earth) - Imagine yourself surrounded by the beauty of a Japanese sacred grove as your body is cleansed and restored to its natural glowing state with the garden-inspired 地 tsuchi (Earth) Cleansing Body Scrub. Himalayan Pink Salts are organic compliant and hand-mined from deep within the Himalayan Mountains. Himalayan Pink Salts were crystallized more than 200 million years ago, when ancient sea beds were covered by volcanic lava, protecting the salt from modern-day pollution and lending to the belief that it is the purest salt to be found on earth. These ancient salts, along with dried blue cornflowers, jasmine flowers and lavender buds, exfoliate dry skin and prepare for an earthy delite. Pure essential oils of geranium rose, palmarosa, cedarwood and lavender calm the senses while increasing circulation and flushing impurities from the skin. Regain the luster your skin once had with the 地 tsuchi (Earth) Cleansing Body Scrub.

Use: Grab a small amount. Massage gently onto surface of dry skin. Add a small amount of warm water and massage gently again. Rinse with warm water, dry and apply 地 tsuchi (Earth) Body Lotion.

Ingredients: Sodium Chloride (Himalayan Pink Salt), Oryza Sativa (Rice) Bran Oil, Carthamus Tinctorius (Safflower) Seed Oil, Caprylic/Capric Triglyceride (Fractionated Coconut Oil), Lavandula Angustifolia (Lavender) Oil, Lavandula Angustifolia (Lavender) Buds, Jasminum Odoratissimum (Jasmine) Flowers, Pelargonium Capitatum X Radens (Rose Geranium) Oil, Tocopherol (Vitamin E), Cupressus Funebris (Chinese Cedarwood) Bark Oil, Centaurea Cyanus (Cornflower), Cymbopogon Martinii Var Motia (Palmarosa) Oil.
_________________________

水 mizu (Water) - Restore your skin’s natural radiance and clarity. 水 mizu (Water) Cleansing Body Scrub uses Japanese Sea salts (among the purest salts in the world) and Israeli Dead Sea salt (rich in nourishing minerals) to exfoliate and reveal refreshed skin. Soy seed aids in exfoliation and also provides lecithin and lipids for repairing and regenerating skin cells. As rosemary oil fights bacteria, improves circulation, and reduces the appearance of broken capillaries and varicose veins, protein-rich sweet almond oil nurtures and soothes. 水 mizu (Water) Cleansing Body Scrub also benefits skin with the anti-inflammatory, antiseptic, and uplifting properties of peppermint, spearmint, and thyme. Protect and replenish your skin with 水 mizu (Water) Cleansing Body Scrub.

Use: Grab a small amount. Massage gently onto surface of dry skin. Add a small amount of warm water and massage gently again. Rinse with warm water, dry and apply 水 mizu (Water) Body Lotion.

Ingredients: Sodium Chloride (Mediterranean Sea and Israeli Dead Sea Salt), Prunus Amygdalus Dulcis (Sweet Almond) Oil, Glycine Soja (Soy) Seeds, Rosmarinus Officinalis (Rosemary) Leaf Oil, Mentha Spicata (Spearmint) Leaf Oil, Mentha Piperita (Peppermint) Leaf, Thymus Zygis (Thyme) Oil, Urtica Dioica (Nettle) Leaf Powder, Tocopherol (Vitamin E).
_________________________

空 sora (Heaven) - Refresh and restore balance to your skin with natural exfoliants including organic evaporated cane sugar, luffa fruit powder, and lavender flower, 空 sora (Heaven) Cleansing Body Scrub rejuvenates dull, dry skin. Sweet almond oil, rich in proteins and vitamin D, nourishes and soothes while vitamin C-rich orange peel stimulates circulation and boosts collagen production. As the soft scent of lavender and patchouli oil calms and relaxes the mind, this scrub detoxifies skin, tones, and eases inflammation with orange oil and pink grapefruit oil. With tocopherol (vitamin E), it also helps diminish the signs of aging and protects skin from sun damage and pollutants. Reveal healthier, more balanced skin with our 空 sora (Heaven) Cleansing Body Scrub.

Use: Grab a small amount. Massage gently onto surface of dry skin. Add a small amount of warm water and massage gently again. Rinse with warm water, dry and apply 空 sora (Heaven) Body Lotion.

Ingredients: Organic Sucrose (Sugar), Prunus Amygdalus Dulcis (Sweet Almond) Oil, Citrus Sinensis (Orange) Peel Oil, Citrus Sinensis (Orange) Peel Powder, Luffa Cylindrica Fruit Powder, Lavandula Angustifolia (Lavender) Buds, Carthamus Tinctorius (Safflower) Powder, Citrus Grandis (Pink Grapefruit) Peel Oil, Lavandula Angustifolia (Lavender) Oil, Pogostemon Cablin (Patchouli) Oil, Tocopherol (Vitamin E).

Industry/Entity Type

Skin Care Product

Font styles to use
Other font styles liked:
• Helvetica Neue Slim for the logo VORELLE

Colors

Designer to choose colors to be used in the design.

Requirements
Must have
• My Labels must have the Japanese Kanji symbols for each of the elements characters. Must also have the brand name VORELLE on the label of each product.

```html
<!DOCTYPE html>
<html lang="en">
<head>
<meta charset="utf-8">
<title>VORELLE Cleansing Body Scrub – Jar Wrap Labels</title>
<link rel="stylesheet" href="https://fonts.googleapis.com/css2?family=Noto+Sans+JP:wght@500&family=Open+Sans:wght@300;400;600&display=swap">
<style>
  :root {
    --canvas: #ffffff;
    --brand-ink: #1c1c1c;
    --copy: #ffffff;

    --fire-base: #dc8034;  --fire-deep: #a8531b;  --fire-light: #e69447;  --fire-mark: #6a3a16;
    --wind-base: #c6c6c6;  --wind-deep: #a9a9a9;  --wind-light: #f0f0f0;  --wind-mark: #6b6b6b;
    --earth-base: #3a8e2f; --earth-deep: #1f7327; --earth-light: #55b039; --earth-mark: #1d561b;
    --water-base: #22649f; --water-deep: #233f95; --water-light: #2f82b5; --water-mark: #1a4470;
    --sky-base: #38b2bc;   --sky-deep: #2a9fc4;   --sky-light: #86d6e2;  --sky-mark: #177e86;
  }

  * { box-sizing: border-box; margin: 0; padding: 0; }

  html, body {
    width: 1200px;
    height: 593px;
    overflow: hidden;
    background: var(--canvas);
  }

  .sheet {
    position: relative;
    width: 1200px;
    height: 593px;
  }

  .label {
    position: absolute;
    width: 499px;
    height: 66px;
    overflow: hidden;
    background: var(--base);
  }

  .label--sheen {
    background: linear-gradient(90deg, var(--light) 0%, var(--base) 30%, var(--light) 55%, var(--base) 75%, var(--deep) 100%);
  }

  .label--fire  { --base: var(--fire-base);  --deep: var(--fire-deep);  --light: var(--fire-light);  --mark: var(--fire-mark); }
  .label--wind  { --base: var(--wind-base);  --deep: var(--wind-deep);  --light: var(--wind-light);  --mark: var(--wind-mark); }
  .label--earth { --base: var(--earth-base); --deep: var(--earth-deep); --light: var(--earth-light); --mark: var(--earth-mark); }
  .label--water { --base: var(--water-base); --deep: var(--water-deep); --light: var(--water-light); --mark: var(--water-mark); }
  .label--sky   { --base: var(--sky-base);   --deep: var(--sky-deep);   --light: var(--sky-light);   --mark: var(--sky-mark); }

  .brand {
    position: absolute;
    left: 40px;
    top: 10px;
    font-family: "Open Sans", sans-serif;
    font-weight: 300;
    font-size: 19px;
    letter-spacing: 1.5px;
    line-height: 1;
    color: var(--brand-ink);
  }

  .product-type {
    position: absolute;
    left: 41px;
    top: 32px;
    font-family: "Open Sans", sans-serif;
    font-weight: 400;
    font-size: 7px;
    line-height: 1;
    color: var(--brand-ink);
  }

  .rule {
    position: absolute;
    left: 0;
    top: 53px;
    width: 110px;
    height: 1px;
    background: var(--brand-ink);
    opacity: 0.75;
  }

  .element-name {
    position: absolute;
    z-index: 2;
    left: 112px;
    top: 47px;
    font-family: "Open Sans", sans-serif;
    font-weight: 400;
    font-size: 10.5px;
    line-height: 1;
    color: var(--copy);
  }

  .kanji {
    position: absolute;
    z-index: 1;
    left: 146px;
    top: 1px;
    font-family: "Noto Sans JP", sans-serif;
    font-weight: 500;
    font-size: 62px;
    line-height: 1;
    color: var(--mark);
  }

  .description {
    position: absolute;
    left: 262px;
    top: 5px;
    width: 228px;
    height: 56px;
    display: flex;
    align-items: center;
    font-family: "Open Sans", sans-serif;
    font-weight: 600;
    font-size: 4px;
    line-height: 5px;
    color: var(--copy);
  }

  .description p {
    text-align: justify;
    text-align-last: center;
  }

  .col-a { left: 70px; }
  .col-b { left: 641px; }
  .row-1 { top: 56px; }
  .row-2 { top: 160px; }
  .row-3 { top: 263px; }
  .row-4 { top: 366px; }
  .row-5 { top: 470px; }
</style>
</head>
<body>
<main class="sheet">

  <!-- Flat colour set -->
  <section class="label label--fire col-a row-1">
    <span class="brand">vorelle</span>
    <span class="product-type">Cleansing Body Scrub</span>
    <span class="rule"></span>
    <span class="element-name">hi</span>
    <span class="kanji" lang="ja">火</span>
    <div class="description"><p>Evoking thoughts of cozying up with a warm cup of chai on a cool autumn night, our Cleansing Body Scrub embodies the virtue of purity while delivering a decadent experience. Organic Japanese honey crystals, organic Japanese black tea and organic sunflower seed oil, exfoliate and renew parched, rough skin while powerful essential oils increase circulation and flush toxins from the skin. Japanese honey, which contains antibacterial, antiseptic, and antioxidant properties, heals and nourishes while glycolic acid, one of honey’s natural alpha hydroxy acids, exfoliates and smooths the skin. As a humectant, honey also revitalizes and soothes overworked, dehydrated skin. Together these powerful ingredients support the skin’s own cell renewal process, and assist in creating smooth, hydrated skin. Rejuvenate, soften, and restore the natural glow of youthful skin with 火 hi (Fire) Cleansing Body Scrub.</p></div>
  </section>

  <section class="label label--wind col-a row-2">
    <span class="brand">vorelle</span>
    <span class="product-type">Cleansing Body Scrub</span>
    <span class="rule"></span>
    <span class="element-name">kaze</span>
    <span class="kanji" lang="ja">風</span>
    <div class="description"><p>Rouse your senses and renew your dull skin with 風 kaze (Wind) Body Scrub. Pure Asian Sea salt and Israeli Dead Sea salt, along with Japanese fruit powders, gently exfoliate to reveal fresher, more vibrant skin. Sweet almond, lavender, and clary sage oils soothe body and mind as lemon peel and oils of rosemary and cajeput heal and improve skin clarity. 風 kaze (Wind) Cleansing Body Scrub also helps protects skin from environmental damage (including UV rays) with the powerful antioxidant, vitamin E. Prepare to show skin that glows with 風 kaze (Wind) Cleansing Body Scrub.</p></div>
  </section>

  <section class="label label--earth col-a row-3">
    <span class="brand">vorelle</span>
    <span class="product-type">Cleansing Body Scrub</span>
    <span class="rule"></span>
    <span class="element-name">tsuchi</span>
    <span class="kanji" lang="ja">土</span>
    <div class="description"><p>Imagine yourself surrounded by the beauty of a Japanese sacred grove as your body is cleansed and restored to its natural glowing state with the garden-inspired 土 tsuchi (Earth) Cleansing Body Scrub. Himalayan Pink Salts are organic compliant and hand-mined from deep within the Himalayan Mountains. Himalayan Pink Salts were crystallized more than 200 million years ago, when ancient sea beds were covered by volcanic lava, protecting the salt from modern-day pollution and lending to the belief that it is the purest salt to be found on earth. These ancient salts, along with dried blue cornflowers, jasmine flowers and lavender buds, exfoliate dry skin and prepare for an earthy delite. Pure essential oils of geranium rose, palmarosa, cedarwood and lavender calm the senses while increasing circulation and flushing impurities from the skin. Regain the luster your skin once had with the 土 tsuchi (Earth) Cleansing Body Scrub.</p></div>
  </section>

  <section class="label label--water col-a row-4">
    <span class="brand">vorelle</span>
    <span class="product-type">Cleansing Body Scrub</span>
    <span class="rule"></span>
    <span class="element-name">mizu</span>
    <span class="kanji" lang="ja">水</span>
    <div class="description"><p>Restore your skin’s natural radiance and clarity. 水 mizu (Water) Cleansing Body Scrub uses Japanese Sea salts (among the purest salts in the world) and Israeli Dead Sea salt (rich in nourishing minerals) to exfoliate and reveal refreshed skin. Soy seed aids in exfoliation and also provides lecithin and lipids for repairing and regenerating skin cells. As rosemary oil fights bacteria, improves circulation, and reduces the appearance of broken capillaries and varicose veins, protein-rich sweet almond oil nurtures and soothes. 水 mizu (Water) Cleansing Body Scrub also benefits skin with the anti-inflammatory, antiseptic, and uplifting properties of peppermint, spearmint, and thyme. Protect and replenish your skin with 水 mizu (Water) Cleansing Body Scrub.</p></div>
  </section>

  <section class="label label--sky col-a row-5">
    <span class="brand">vorelle</span>
    <span class="product-type">Cleansing Body Scrub</span>
    <span class="rule"></span>
    <span class="element-name">sora</span>
    <span class="kanji" lang="ja">天</span>
    <div class="description"><p>Refresh and restore balance to your skin with natural exfoliants including organic evaporated cane sugar, luffa fruit powder, and lavender flower, 天 sora (Heaven) Cleansing Body Scrub rejuvenates dull, dry skin. Sweet almond oil, rich in proteins and vitamin D, nourishes and soothes while vitamin C-rich orange peel stimulates circulation and boosts collagen production. As the soft scent of lavender and patchouli oil calms and relaxes the mind, this scrub detoxifies skin, tones, and eases inflammation with orange oil and pink grapefruit oil. With tocopherol (vitamin E), it also helps diminish the signs of aging and protects skin from sun damage and pollutants. Reveal healthier, more balanced skin with our 天 sora (Heaven) Cleansing Body Scrub.</p></div>
  </section>

  <!-- Gradient sheen set -->
  <section class="label label--fire label--sheen col-b row-1">
    <span class="brand">vorelle</span>
    <span class="product-type">Cleansing Body Scrub</span>
    <span class="rule"></span>
    <span class="element-name">hi</span>
    <span class="kanji" lang="ja">火</span>
    <div class="description"><p>Evoking thoughts of cozying up with a warm cup of chai on a cool autumn night, our Cleansing Body Scrub embodies the virtue of purity while delivering a decadent experience. Organic Japanese honey crystals, organic Japanese black tea and organic sunflower seed oil, exfoliate and renew parched, rough skin while powerful essential oils increase circulation and flush toxins from the skin. Japanese honey, which contains antibacterial, antiseptic, and antioxidant properties, heals and nourishes while glycolic acid, one of honey’s natural alpha hydroxy acids, exfoliates and smooths the skin. As a humectant, honey also revitalizes and soothes overworked, dehydrated skin. Together these powerful ingredients support the skin’s own cell renewal process, and assist in creating smooth, hydrated skin. Rejuvenate, soften, and restore the natural glow of youthful skin with 火 hi (Fire) Cleansing Body Scrub.</p></div>
  </section>

  <section class="label label--wind label--sheen col-b row-2">
    <span class="brand">vorelle</span>
    <span class="product-type">Cleansing Body Scrub</span>
    <span class="rule"></span>
    <span class="element-name">kaze</span>
    <span class="kanji" lang="ja">風</span>
    <div class="description"><p>Rouse your senses and renew your dull skin with 風 kaze (Wind) Body Scrub. Pure Asian Sea salt and Israeli Dead Sea salt, along with Japanese fruit powders, gently exfoliate to reveal fresher, more vibrant skin. Sweet almond, lavender, and clary sage oils soothe body and mind as lemon peel and oils of rosemary and cajeput heal and improve skin clarity. 風 kaze (Wind) Cleansing Body Scrub also helps protects skin from environmental damage (including UV rays) with the powerful antioxidant, vitamin E. Prepare to show skin that glows with 風 kaze (Wind) Cleansing Body Scrub.</p></div>
  </section>

  <section class="label label--earth label--sheen col-b row-3">
    <span class="brand">vorelle</span>
    <span class="product-type">Cleansing Body Scrub</span>
    <span class="rule"></span>
    <span class="element-name">tsuchi</span>
    <span class="kanji" lang="ja">土</span>
    <div class="description"><p>Imagine yourself surrounded by the beauty of a Japanese sacred grove as your body is cleansed and restored to its natural glowing state with the garden-inspired 土 tsuchi (Earth) Cleansing Body Scrub. Himalayan Pink Salts are organic compliant and hand-mined from deep within the Himalayan Mountains. Himalayan Pink Salts were crystallized more than 200 million years ago, when ancient sea beds were covered by volcanic lava, protecting the salt from modern-day pollution and lending to the belief that it is the purest salt to be found on earth. These ancient salts, along with dried blue cornflowers, jasmine flowers and lavender buds, exfoliate dry skin and prepare for an earthy delite. Pure essential oils of geranium rose, palmarosa, cedarwood and lavender calm the senses while increasing circulation and flushing impurities from the skin. Regain the luster your skin once had with the 土 tsuchi (Earth) Cleansing Body Scrub.</p></div>
  </section>

  <section class="label label--water label--sheen col-b row-4">
    <span class="brand">vorelle</span>
    <span class="product-type">Cleansing Body Scrub</span>
    <span class="rule"></span>
    <span class="element-name">mizu</span>
    <span class="kanji" lang="ja">水</span>
    <div class="description"><p>Restore your skin’s natural radiance and clarity. 水 mizu (Water) Cleansing Body Scrub uses Japanese Sea salts (among the purest salts in the world) and Israeli Dead Sea salt (rich in nourishing minerals) to exfoliate and reveal refreshed skin. Soy seed aids in exfoliation and also provides lecithin and lipids for repairing and regenerating skin cells. As rosemary oil fights bacteria, improves circulation, and reduces the appearance of broken capillaries and varicose veins, protein-rich sweet almond oil nurtures and soothes. 水 mizu (Water) Cleansing Body Scrub also benefits skin with the anti-inflammatory, antiseptic, and uplifting properties of peppermint, spearmint, and thyme. Protect and replenish your skin with 水 mizu (Water) Cleansing Body Scrub.</p></div>
  </section>

  <section class="label label--sky label--sheen col-b row-5">
    <span class="brand">vorelle</span>
    <span class="product-type">Cleansing Body Scrub</span>
    <span class="rule"></span>
    <span class="element-name">sora</span>
    <span class="kanji" lang="ja">天</span>
    <div class="description"><p>Refresh and restore balance to your skin with natural exfoliants including organic evaporated cane sugar, luffa fruit powder, and lavender flower, 天 sora (Heaven) Cleansing Body Scrub rejuvenates dull, dry skin. Sweet almond oil, rich in proteins and vitamin D, nourishes and soothes while vitamin C-rich orange peel stimulates circulation and boosts collagen production. As the soft scent of lavender and patchouli oil calms and relaxes the mind, this scrub detoxifies skin, tones, and eases inflammation with orange oil and pink grapefruit oil. With tocopherol (vitamin E), it also helps diminish the signs of aging and protects skin from sun damage and pollutants. Reveal healthier, more balanced skin with our 天 sora (Heaven) Cleansing Body Scrub.</p></div>
  </section>

</main>
</body>
</html>
```